3 -4 PAGE GIFT CERTIFICATE REDEMPTION WEBSITE REVAMP

I am revamping the entire website at www.brightperksportal.net

Will have brand new theme and new logo. Name Of Company:
Bounty Motivation Delivery Networks
BMDN

OVERVIEW:
I NEED A 3-4 PAGE WEBSITE DESIGNED WITH CHECKOUT MODULE.
My company offers fully brandable and personalizable gift certificates good for travel, vacations, dining rewards, rebates, electronic gifts, etc. and I need to redesign the website where the fulfillment and redemption happens.

So the way it works is a business uses my online platform to create, brand and personalize these gift certificates. The business can brand the certificates in the upper right hand corner of each certificate where the “Compliments Of” area sits with their company logo, website, contact info, etc and can also personalize each individual gift certificate to a specific customer too. SEE EXAMPLE ATTACHED TO BRIEF.

The example I attached to this brief includes a logo which is really just a picture and under it there is 3 lines of text where the business can put a website, phone number and email.

On the left side of the top banner image you will see “Exclusively For”.

So now, after a customer enters their certificate ID #, the branding on the next page must match the Compliments Of area and also must personalize the Sales Page to the customer that is in the Exclusively For” area of the certificate…...

Page 1: LANDING PAGE
CONTENT:

Welcome to the online redemption source for vacation certificates, travel vouchers, digital electronic products, dining incentives, gas and grocery rewards and more!

ENTER YOUR CERTIFICATE ID #
ENTER YOUR EMAIL

Welcome to the online redemption system for vacation certificates, travel vouchers, rebates, digital products, dining incentives, gas and grocery rewards and more!

PLEASE ENTER A VALID CERTIFICATE ID NUMBER TO VIEW THE DETAILS AND TO REDEEM AND ACTIVATE YOUR SPECIAL OFFER.

Also we need a testimonial module ON THIS PAGE AND SALES PAGE

PAGE 2: SALES PAGE FOR OFFER (we will use the 1-4 Night Las Vegas Hotel Stay Certificate)
INSTRUCTIONS EXPLANATION FOR DESIGNER: Every gift certificate has a "Compliments Of Area" in the upper right hand corner....SEE SAMPLE ATTACHED TO BRIEF. On the sales page we also show this to the customer after they enter the code. Every certificate has a Compliments Of area and we will also add "Exclusively For" so the person that is giving the certificate away can specify the name of the recipient so we will also transffer this information over to the SALES PAGE.

CONTENT FOR SALES PAGE:

WELCOME ~~NAME OF PERSON IN EXCLUSIVELY FOR AREA ON CERTIFICATE~~ !!

THIS SPECIAL INCENTIVE OFFER IS COMPLIMENTS OF

~~LOGO THAT IS SEEN ON CERTIFICATE~~
~~TEXT LINE 1~~
~~TEXT LINE 2~~
~~TEXT LINE 3~~

TITLE OF OFFER: STAY & PLAY IN LAS VEGAS FOR UP TO 4 NIGHTS!
There is no doubt that Las Vegas is one of the hottest travel destinations around the world. In fact, some people would even go as far as saying that perhaps it is THE hottest place to visit. Enjoy up to 4 nights of resort/casino accommodations in exciting Las Vegas, NV. Millions of people travel to this exciting city each year to enjoy its thrills. Thanks to the business you received this certificate from, now you can enjoy Las Vegas, NV too!

Features:
*Travel 7 Days A Week
*Stay Your Choice Of Nights (1-4 Nights)
*Good For Two Adults & Two Children
*Pay Just The Taxes & Fees
*Multiple Travel Date Requests Allowed
*Fully Transferable To Another Person
*Just A 30 Days Advance Notice Required
*You Will Have 12 Months To Complete Travel

HOW CAN WE DO THIS?

We contract with the world leading hotel chains and resorts to help them fill their otherwise empty rooms.

We help fill empty rooms which the hotels, resorts and cruise lines turn into additional revenue from other areas of their property and future bookings.

Hotels rarely experience full occupancy, yet they remain open, providing rooms and services at fixed costs. So when hotels give out their rooms by partnering with marketing companies like us, they might miss out on the room fee, but they already didn't have that in the first place, at least now they have the opportunity to gain a customer for their in-house restaurants, room service, their casinos, an extra day stay, future bookings, etc.

The magic of why our program works so well is the fact that it’s a win win for everyone involved. You win because you received a huge savings. The business who gave you the certificate wins because now you will remember them the next time you need the same kind of product or service that they provide and you might even refer your friends and family members. The hotels and resorts win because they gain additional revenue from other areas of their establishment that they otherwise would not have been able to get and they also have a new client that may book with them in the future. Remember, they didn’t have anyone in the room in the first place so since you are paying the normal rack rate you might be more inclined to spend your money at the hotel. You are never under any obligation to do so though!

Retail Value: Up to $826.00 (based on $159.00 per night)

How it Works:
You will receive up to 4 nights in a 3 star or better Las Vegas resort and casino for up to 4 travelers, 2 adults and 2 children.

Simply redeem the certificate to activate the travel period for 1 year. This means you will have at least 1 year to travel from the date you redeem and activate your offer. Be sure to redeem your certificate before it expires! All certificates will have an accompanying expiration date attached to them.

When you are ready to book you will simply have to pay the daily room rate taxes and fees of approximately $12-$33 per night (not per person). On average the taxes and fees come out to about $19 per night. (Retail Value: Up to $826.00 based on $159.00 per night)

Step 1: Redeem your certificate to activate your offer

Step 2: Fill out the online reservation request form with travel dates within the next 12 months.

Step 3: Wait for a confirmation of your booked reservation. You will be notified immediately upon us booking your reservation.

Go on your vacation and thank the business who gave you this special offer by doing business with them again and referring your friends and family members!

No timeshares or sales presentations, Guaranteed!

PAGE 3 IS CHECKOUT PAGE:

PLEASE USE ****HERE IS SAMPLE CODE FOR YOU TO TEST OUT AT CURRENT REDEMPTION PROCESS WWW.BRIGHTPERKSPORTAL.NET 46205-17938

TO SEE THE CURRENT CHECK OUT. I NEED ALL THE SAME CONTENT JUST A DIFFERENT MORE EFFICIENT CHECKOUT PROCESS HERE. OMIT THE LEFT SIDE OF THE CURRENT CHECK OUT PROCESS AS THIS CURRENT PROCESSS IS ONE STEP AND DOES NOT HAVE A SALES PAGE BUT NOW I AM CREATING A SALES PAGE BEFORE THE CHECKOUT SO THE BRANDING AND PERSONALIZATION WILL HAPPEN ON THE SALES PAGE….THANK YOU

Target Market(s)

END USERS THAT ARE REDEEMING SPECIAL OFFERS GIFT CERTIFICATES

Industry/Entity Type

Marketing

Number of Pages Required

4 page

Colors

Designer to choose colors to be used in the design.

Requirements
Must have
• OVERVIEW:
• I NEED A 3-4 PAGE WEBSITE DESIGNED WITH CHECKOUT MODULE.
• My company offers fully brandable and personalizable gift certificates good for travel, vacations, dining rewards, rebates, electronic gifts, etc. and I need to redesign the website where the fulfillment and redemption happens.
• So the way it works is a business uses my online platform to create, brand and personalize these gift certificates. The business can brand the certificates in the upper right hand corner of each certificate where the “Compliments Of” area sits with their company logo, website, contact info, etc and can also personalize each individual gift certificate to a specific customer too. SEE EXAMPLE ATTACHED TO BRIEF.
• The example I attached to this brief includes a logo which is really just a picture and under it there is 3 lines of text where the business can put a website, phone number and email.
• On the left side of the top banner image you will see “Exclusively For”.
• So now, after a customer enters their certificate ID #, the branding on the next page must match the Compliments Of area and also must personalize the Sales Page to the customer that is in the Exclusively For” area of the certificate…...
• Page 1: LANDING PAGE
• CONTENT:
• Welcome to the online redemption source for vacation certificates, travel vouchers, digital electronic products, dining incentives, gas and grocery rewards and more!
• ENTER YOUR CERTIFICATE ID #
• ENTER YOUR EMAIL
• Welcome to the online redemption system for vacation certificates, travel vouchers, rebates, digital products, dining incentives, gas and grocery rewards and more!
• PLEASE ENTER A VALID CERTIFICATE ID NUMBER TO VIEW THE DETAILS AND TO REDEEM AND ACTIVATE YOUR SPECIAL OFFER.
• Also we need a testimonial module ON THIS PAGE AND SALES PAGE
• PAGE 2: SALES PAGE FOR OFFER (we will use the 1-4 Night Las Vegas Hotel Stay Certificate)
• INSTRUCTIONS EXPLANATION FOR DESIGNER: Every gift certificate has a "Compliments Of Area" in the upper right hand corner....SEE SAMPLE ATTACHED TO BRIEF. On the sales page we also show this to the customer after they enter the code. Every certificate has a Compliments Of area and we will also add "Exclusively For" so the person that is giving the certificate away can specify the name of the recipient so we will also transffer this information over to the SALES PAGE.
• CONTENT FOR SALES PAGE:
• WELCOME ~~NAME OF PERSON IN EXCLUSIVELY FOR AREA ON CERTIFICATE~~ !!
• THIS SPECIAL INCENTIVE OFFER IS COMPLIMENTS OF
• ~~LOGO THAT IS SEEN ON CERTIFICATE~~
• ~~TEXT LINE 1~~
• ~~TEXT LINE 2~~
• ~~TEXT LINE 3~~
• TITLE OF OFFER: STAY & PLAY IN LAS VEGAS FOR UP TO 4 NIGHTS!
• There is no doubt that Las Vegas is one of the hottest travel destinations around the world. In fact, some people would even go as far as saying that perhaps it is THE hottest place to visit. Enjoy up to 4 nights of resort/casino accommodations in exciting Las Vegas, NV. Millions of people travel to this exciting city each year to enjoy its thrills. Thanks to the business you received this certificate from, now you can enjoy Las Vegas, NV too!
• Features:
• *Travel 7 Days A Week
• *Stay Your Choice Of Nights (1-4 Nights)
• *Good For Two Adults & Two Children
• *Pay Just The Taxes & Fees
• *Multiple Travel Date Requests Allowed
• *Fully Transferable To Another Person
• *Just A 30 Days Advance Notice Required
• *You Will Have 12 Months To Complete Travel
• HOW CAN WE DO THIS?
• We contract with the world leading hotel chains and resorts to help them fill their otherwise empty rooms.
• We help fill empty rooms which the hotels, resorts and cruise lines turn into additional revenue from other areas of their property and future bookings.
• Hotels rarely experience full occupancy, yet they remain open, providing rooms and services at fixed costs. So when hotels give out their rooms by partnering with marketing companies like us, they might miss out on the room fee, but they already didn't have that in the first place, at least now they have the opportunity to gain a customer for their in-house restaurants, room service, their casinos, an extra day stay, future bookings, etc.
• The magic of why our program works so well is the fact that it’s a win win for everyone involved. You win because you received a huge savings. The business who gave you the certificate wins because now you will remember them the next time you need the same kind of product or service that they provide and you might even refer your friends and family members. The hotels and resorts win because they gain additional revenue from other areas of their establishment that they otherwise would not have been able to get and they also have a new client that may book with them in the future. Remember, they didn’t have anyone in the room in the first place so since you are paying the normal rack rate you might be more inclined to spend your money at the hotel. You are never under any obligation to do so though!
• Retail Value: Up to $826.00 (based on $159.00 per night)
• How it Works:
• You will receive up to 4 nights in a 3 star or better Las Vegas resort and casino for up to 4 travelers, 2 adults and 2 children.
• Simply redeem the certificate to activate the travel period for 1 year. This means you will have at least 1 year to travel from the date you redeem and activate your offer. Be sure to redeem your certificate before it expires! All certificates will have an accompanying expiration date attached to them.
• When you are ready to book you will simply have to pay the daily room rate taxes and fees of approximately $12-$33 per night (not per person). On average the taxes and fees come out to about $19 per night. (Retail Value: Up to $826.00 based on $159.00 per night)
• Step 1: Redeem your certificate to activate your offer
• Step 2: Fill out the online reservation request form with travel dates within the next 12 months.
• Step 3: Wait for a confirmation of your booked reservation. You will be notified immediately upon us booking your reservation.
• Go on your vacation and thank the business who gave you this special offer by doing business with them again and referring your friends and family members!
• No timeshares or sales presentations, Guaranteed!
• PAGE 3 IS CHECKOUT PAGE:
• PLEASE USE ****HERE IS SAMPLE CODE FOR YOU TO TEST OUT AT CURRENT REDEMPTION PROCESS WWW.BRIGHTPERKSPORTAL.NET 46205-17938
• TO SEE THE CURRENT CHECK OUT. I NEED ALL THE SAME CONTENT JUST A DIFFERENT MORE EFFICIENT CHECKOUT PROCESS HERE. OMIT THE LEFT SIDE OF THE CURRENT CHECK OUT PROCESS AS THIS CURRENT PROCESSS IS ONE STEP AND DOES NOT HAVE A SALES PAGE BUT NOW I AM CREATING A SALES PAGE BEFORE THE CHECKOUT SO THE BRANDING AND PERSONALIZATION WILL HAPPEN ON THE SALES PAGE….THANK YOU
Nice to have
• OVERVIEW:
• Page 1: LANDING PAGE
• CONTENT:
• ENTER YOUR EMAIL
• CONTENT FOR SALES PAGE:
• ~~TEXT LINE 1~~
• ~~TEXT LINE 2~~
• ~~TEXT LINE 3~~
• Features:
• *Travel 7 Days A Week
• HOW CAN WE DO THIS?
• How it Works:
Should not have
• OVERVIEW:
• Page 1: LANDING PAGE
• CONTENT:
• ENTER YOUR EMAIL
• CONTENT FOR SALES PAGE:
• ~~TEXT LINE 1~~
• ~~TEXT LINE 2~~
• ~~TEXT LINE 3~~
• Features:
• *Travel 7 Days A Week
• HOW CAN WE DO THIS?
• How it Works:

```html
<!DOCTYPE html>
<html lang="en">
<head>
<meta charset="utf-8">
<title>BrightPerksPortal – Redemption Source</title>
<link href="https://fonts.googleapis.com/css2?family=Archivo:wght@400;700&family=Lato:wght@400;700&family=Roboto+Condensed:ital,wght@1,300&display=swap" rel="stylesheet">
<style>
:root{
  --orange:#f47321;
  --ink:#111111;
  --text:#2b2b2b;
  --muted:#6e6e6e;
  --white:#ffffff;
  --footer:#0c0c0c;
  --canyon-dark:#4a2a22;
  --canyon:#8a4a35;
  --canyon-light:#b77a5c;
}
*{margin:0;padding:0;box-sizing:border-box}
html,body{width:880px;height:1200px;overflow:hidden;background:var(--white)}
body{position:relative;font-family:"Archivo",Arial,sans-serif;color:var(--text)}
.abs{position:absolute}

.site-header{position:absolute;left:0;top:0;width:880px;height:53px;background:var(--white);z-index:3}
.brand{left:96px;top:15px;font-weight:700;font-size:12px;color:var(--orange);line-height:1}
.brand-sub{left:110px;top:30px;font-size:4px;color:var(--text)}
.brand-tag{left:112px;top:40px;font-size:7.5px;color:var(--muted)}
.nav a{position:absolute;top:22px;font-size:10px;color:var(--ink);text-decoration:none}

.hero{position:absolute;left:0;top:53px;width:880px;height:478px;
  background:linear-gradient(100deg,var(--canyon-dark) 0%,var(--canyon) 40%,var(--canyon-light) 65%,#7d5445 100%)}
.hero-shade{position:absolute;inset:0;background:linear-gradient(90deg,rgba(30,15,10,.45),rgba(30,15,10,.05) 70%)}
.hero-wave{position:absolute;left:0;top:53px;width:880px;height:478px}
.hero-title{left:82px;top:188px;font-size:30px;font-weight:700;line-height:32px;color:var(--white)}
.hero-lead{left:82px;top:262px;width:430px;font-size:10.7px;line-height:16px;color:var(--white)}
.hero-note{left:82px;top:302px;width:430px;font-size:10.7px;line-height:16px;color:var(--white)}
.cert-field{left:82px;top:343px;width:201px;height:25px;background:var(--white);border:0}
.cert-go{left:283px;top:343px;width:45px;height:25px;background:var(--orange);color:var(--white);
  font-size:7.5px;display:flex;align-items:center;justify-content:center}

.section-title{left:0;width:910px;top:540px;text-align:center;font-size:38px;font-weight:700;color:var(--ink)}
.testimonial-card{left:112px;top:624px;width:652px;height:340px;background:var(--white);box-shadow:0 0 8px rgba(0,0,0,.25)}
.reviewer{left:112px;width:684px;top:642px;text-align:center;font-size:28px;font-weight:700;color:var(--text)}
.reviewer-rule{left:459px;top:687px;width:219px;height:1.5px;background:#eea77b}
.reviewer-place{left:459px;top:697px;font-size:10px;letter-spacing:4.5px;color:var(--muted)}
.reviewer-photo{left:186px;top:690px;width:212px;height:200px;background:linear-gradient(160deg,#b9b9b6,#6e7077 55%,#27324f)}
.quote-mark{left:608px;top:790px;font-family:Georgia,serif;font-size:140px;line-height:1;color:#e3e3e3;font-weight:700}
.quote-text{left:456px;top:735px;width:234px;font-family:"Roboto Condensed",Arial,sans-serif;font-style:italic;font-weight:300;
  font-size:10.6px;line-height:23.3px;color:#5a5a5a;text-align:justify;text-align-last:center}
.slide-btn{width:47px;height:49px;background:var(--orange);display:flex;align-items:center;justify-content:center}
.slide-prev{left:89px;top:769px}
.slide-next{left:741px;top:769px}

.site-footer{position:absolute;left:0;top:1020px;width:880px;height:180px;background:var(--footer);font-family:"Lato",Arial,sans-serif;color:var(--white)}
.foot-col{position:absolute;top:26px}
.foot-col h4{font-size:11.5px;font-weight:700;margin-bottom:7px}
.foot-col li{list-style:none;font-size:9px;line-height:17.2px}
.social{display:flex;gap:8px;margin-top:4px}
.social span{width:19px;height:19px;border:2px solid var(--white)}
.foot-rule{position:absolute;left:0;top:152px;width:880px;height:1px;background:#7a3a12}
.copyright{position:absolute;left:0;width:918px;top:161px;text-align:center;font-size:9px}
</style>
</head>
<body>

<header class="site-header">
  <div class="abs brand">BrightPerksPortal</div>
  <div class="abs brand-sub">Redemption Processing Center</div>
  <div class="abs brand-tag">Exclusively For</div>
  <nav class="nav">
    <a style="left:433px">Home</a>
    <a style="left:503px">Page</a>
    <a style="left:570px">Contact Us</a>
    <a style="left:664px">Testimonials</a>
    <a style="left:764px">Terms</a>
  </nav>
</header>

<section class="hero" role="img" aria-label="Desert road through red canyon cliffs with a yellow camper van driving away">
  <div class="hero-shade"></div>
</section>
<svg class="hero-wave" viewBox="0 0 880 478" aria-hidden="true">
  <path d="M0 478 C 60 420, 170 408, 290 408 C 420 410, 520 452, 620 450 C 730 448, 820 432, 880 410 V 478 Z" fill="#ffffff"/>
</svg>

<h1 class="abs hero-title">Welcome To The<br>Redemption Source</h1>
<p class="abs hero-lead">Welcome to the online redemption system for vacation certificates, travel vouchers, rebates, digital products, dining incentives, gas and grocery rewards and more!</p>
<p class="abs hero-note">PLEASE ENTER A VALID CERTIFICATE ID NUMBER TO VIEW THE DETAILS AND TO REDEEM AND ACTIVATE YOUR SPECIAL OFFER.</p>
<div class="abs cert-field"></div>
<div class="abs cert-go">GO</div>

<h2 class="abs section-title">Testimonials</h2>

<div class="abs testimonial-card"></div>
<div class="abs reviewer">Darren M</div>
<div class="abs reviewer-rule"></div>
<div class="abs reviewer-place">Fairview, GA</div>
<div class="abs reviewer-photo" role="img" aria-label="Portrait of a smiling customer in a suit giving a thumbs up"></div>
<div class="abs quote-mark">&ldquo;</div>
<p class="abs quote-text">"I worked with the travel agency and they were very patient with me as I narrowed down where myself and another friend wanted to travel to. I gave them destinations and in return they gave me prompt responses on what was available and in our budget. Don't hesitate to work with this travel agency.....because I won't!"</p>

<div class="abs slide-btn slide-prev">
  <svg width="22" height="18" viewBox="0 0 22 18"><path d="M20 9H4M10 2L3 9l7 7" stroke="#fff" stroke-width="3" fill="none"/></svg>
</div>
<div class="abs slide-btn slide-next">
  <svg width="22" height="18" viewBox="0 0 22 18"><path d="M2 9h16M12 2l7 7-7 7" stroke="#fff" stroke-width="3" fill="none"/></svg>
</div>

<footer class="site-footer">
  <div class="foot-col" style="left:116px">
    <h4>Brightperksportal</h4>
    <ul><li>About Us</li><li>Blog</li><li>Testimonials</li><li>Guides</li><li>Visa</li><li>Press</li></ul>
  </div>
  <div class="foot-col" style="left:294px">
    <h4>Policy</h4>
    <ul><li>Frequently Asked Questions</li><li>Terms &amp; Conditions</li><li>Privacy</li><li>Cancellations</li><li>Sitemap</li><li>Contact Us</li></ul>
  </div>
  <div class="foot-col" style="left:489px">
    <h4>Talk to us</h4>
    <ul><li>planners@brightperksportal.net</li><li>+1 555 014 2290</li><li>Sign up for travel ideas!</li></ul>
  </div>
  <div class="foot-col" style="left:713px">
    <h4>Follow Us:</h4>
    <div class="social"><span></span><span></span><span></span></div>
  </div>
  <div class="foot-rule"></div>
  <div class="copyright">© 2020 all rights reserved.</div>
</footer>

</body>
</html>
```